Acoustic Jazz album needs cover design

The CD cover has five parts, each one has obligatory features:

I. Main cover

Title: Declarations: Sunrise Chants
Artist: Beren Holvathy
Design image*

The main design motive should be something that suggests: happiness, freedom, health, balance, something like that. Please see my other covers at berentones.net/music. Please don’t use the same key elements as there.
I prefer zen-like, minimalist solutions.
NO stock images, please! Except for unrecognizable parts of something.

II. Cover inside

Track list (10 songs) with durations
All songs written by Beren Holvathy
Copyright Berentones 2016.
Design image

III. Disc

Artist: Beren Holvathy
All songs written by Beren Holvathy (round on the edge)
Copyright Berentones 2016. (round on the edge)
www.berentones.net (round on the edge)

IV. Cover back

Track list (same as cover inside)
Copyright Berentones 2016.
www.berentones.net
design image (optional)
The paper of this page is longer than the main cover, because it is to be turned up when put in the CD case, and there is the saddle/spine with the name of the Artist and Title of the album. On both ends.

V. Under the disc

No words, only some design feature.

Important:
The main cover I need in RGB and also CMYK, all the others only CMYK.
I need the work file (cdr, ai or whatever you use)
I need the CMYK images prepared for printing (sizes set, and that little extra on the edges).
I need the RGB main cover cover in jpeg, 3000x3000 pixels.
That's all. :)

The most important of these all is of course the main cover RGB. Make this one first!

Here’s a sample to listen, it might inspire you:

https://www.filevault-share.net/s/k2mq81xz5pwe0vn/sunrise_chants_medley_beren_holvathy_20160108.mp3?dl=0

And here’s the Beren Holvathy logo:

https://www.filevault-share.net/s/tn4vd7rw0yq2hc6/Logo%20BH%20print%2020150216.psd?dl=0

If you take a closer look at my website, you can see the whole concept.

Good luck and enjoy!
Regards,
Beren

Target Market(s)

New age spiritual people

Requirements
Nice to have
• "Simplicity, the ultimate sophistication."
• Don't overdose it with elements. Make it simple.

```html
<!DOCTYPE html>
<html lang="en">
<head>
<meta charset="utf-8">
<title>Declarations: Sunrise Chants — CD Packaging</title>
<link href="https://fonts.googleapis.com/css2?family=Baloo+2:wght@400;600&family=Open+Sans:ital,wght@0,400;0,700;1,400&display=swap" rel="stylesheet">
<style>
  :root {
    --backdrop: #ececec;
    --paper: #f7f7f7;
    --paper-edge: #e3e3e3;
    --ink: #1e1e1e;
    --ink-soft: #3a3a3a;
    --gold: #f3b325;
    --gold-deep: #e0a01a;
    --gold-light: #f8cc5a;
    --cloud: #ffffff;
    --shadow: rgba(0,0,0,0.12);
  }
  * { box-sizing: border-box; margin: 0; padding: 0; }
  html, body { width: 1200px; height: 1200px; overflow: hidden; }
  body {
    background: var(--backdrop);
    font-family: "Open Sans", sans-serif;
    color: var(--ink);
    position: relative;
  }
  .panel {
    position: absolute;
    background: radial-gradient(ellipse at 50% 40%, #ffffff 0%, var(--paper) 60%, var(--paper-edge) 100%);
    box-shadow: 0 6px 16px var(--shadow);
  }
  .front-cover { left: 140px; top: 170px; width: 420px; height: 400px; }
  .back-cover  { left: 640px; top: 170px; width: 450px; height: 400px; }
  .inside-cover { left: 30px; top: 620px; width: 420px; height: 410px; }
  .disc-tray { left: 470px; top: 620px; width: 460px; height: 410px; }

  .artist-name {
    position: absolute;
    font-family: "Baloo 2", sans-serif;
    font-weight: 400;
    color: var(--ink-soft);
    white-space: nowrap;
  }
  .artist-mark {
    display: inline-block;
    width: 10px; height: 10px;
    border-radius: 50%;
    background: var(--gold);
    margin-right: 7px;
    vertical-align: 1px;
  }
  .front-cover .artist-name { left: 0; right: 0; top: 80px; text-align: center; font-size: 19px; }

  .bird-art {
    position: absolute;
    border-radius: 6px;
    background: linear-gradient(135deg, var(--gold-light) 0%, var(--gold) 50%, var(--gold-deep) 100%);
  }
  .bird-shadow {
    position: absolute;
    height: 6px;
    border-radius: 50%;
    background: radial-gradient(ellipse, rgba(0,0,0,0.18), transparent 70%);
  }
  .front-cover .bird-art { left: 115px; top: 145px; width: 235px; height: 165px; }
  .front-cover .bird-shadow { left: 135px; top: 330px; width: 170px; }

  .album-title {
    font-family: "Baloo 2", sans-serif;
    font-weight: 400;
    color: var(--ink);
    line-height: 1.05;
    white-space: nowrap;
  }
  .album-title strong { font-weight: 600; }
  .front-cover .album-title {
    position: absolute; left: 0; right: 0; top: 340px;
    text-align: center; font-size: 20px;
  }

  .credit-block {
    position: absolute;
    text-align: right;
  }
  .credit-block .album-title { font-size: 21px; }
  .credit-line { font-size: 8.5px; line-height: 14px; color: var(--ink-soft); }
  .credit-web { font-family: "Baloo 2", sans-serif; font-weight: 600; font-size: 11.5px; margin-top: 3px; letter-spacing: 0.4px; }

  .track-list {
    position: absolute;
    list-style: none;
    font-size: 9.5px;
    color: var(--ink-soft);
  }
  .track-list li { display: flex; height: 18.8px; align-items: center; }
  .track-no { width: 18px; text-align: right; font-weight: 700; color: var(--ink); margin-right: 8px; }
  .track-name { width: 98px; }
  .track-time { font-style: italic; }

  .back-cover .bird-art { left: 35px; top: 35px; width: 210px; height: 150px; }
  .back-cover .bird-shadow { left: 70px; top: 205px; width: 160px; }
  .back-cover .credit-block { right: 190px; top: 268px; }
  .back-cover .track-list { left: 255px; top: 172px; }

  .cloud-band {
    position: absolute;
    left: 15px; right: 0; top: 30px; height: 95px;
    background: linear-gradient(180deg, rgba(255,255,255,0.95), rgba(255,255,255,0.5));
    border-radius: 50px 50px 6px 6px;
  }
  .inside-cover .credit-block { right: 150px; top: 300px; }
  .inside-cover .track-list { left: 270px; top: 140px; }

  .disc-tray .cloud-band { left: 30px; right: 20px; top: 30px; opacity: 0.8; }
  .tray-ring {
    position: absolute; left: 55px; top: 20px; width: 370px; height: 370px;
    border-radius: 50%;
    background: radial-gradient(circle, #f4f4f4 0%, #ffffff 70%, #ededed 100%);
    border: 1px solid #e2e2e2;
  }

  .disc { position: absolute; left: 790px; top: 695px; width: 400px; height: 400px; }
  .disc .bird-art { left: 165px; top: 38px; width: 95px; height: 65px; }
  .disc .bird-shadow { left: 170px; top: 107px; width: 80px; }
  .disc .album-title { position: absolute; left: 0; right: 0; top: 118px; text-align: center; font-size: 15px; }
  .disc .artist-name { left: 0; right: 0; top: 330px; text-align: center; font-size: 12px; }
  .disc-edge-text { font-family: "Open Sans", sans-serif; font-size: 10.5px; fill: var(--ink); }
  .disc-edge-text .strong { font-weight: 700; }
</style>
</head>
<body>

<section class="panel front-cover" aria-label="Main cover">
  <div class="artist-name"><span class="artist-mark"></span>Beren Holvathy</div>
  <div class="bird-art" role="img" aria-label="Golden origami bird with small white clouds on its wing"></div>
  <div class="bird-shadow"></div>
  <h1 class="album-title"><strong>Declarations:</strong> Sunrise Chants</h1>
</section>

<section class="panel back-cover" aria-label="Back cover">
  <div class="bird-art" role="img" aria-label="Golden origami bird with small white clouds on its wing"></div>
  <div class="bird-shadow"></div>
  <div class="credit-block">
    <h2 class="album-title"><strong>Declarations:</strong><br>Sunrise Chants</h2>
    <p class="credit-line" style="margin-top:6px">All songs written by Beren Holvathy</p>
    <p class="credit-line">Copyright Berentones 2016</p>
    <p class="credit-web">www.berentones.net</p>
  </div>
  <ol class="track-list">
    <li><span class="track-no">1</span><span class="track-name">Piano Relax</span><span class="track-time">5:30</span></li>
    <li><span class="track-no">2</span><span class="track-name">Relax dummy copy</span><span class="track-time">4:15</span></li>
    <li><span class="track-no">3</span><span class="track-name">Relax dummy</span><span class="track-time">6:10</span></li>
    <li><span class="track-no">4</span><span class="track-name">Dummy Relax</span><span class="track-time">3:45</span></li>
    <li><span class="track-no">5</span><span class="track-name">Piano Relax</span><span class="track-time">7:15</span></li>
    <li><span class="track-no">6</span><span class="track-name">Relax dummy copy</span><span class="track-time">5:30</span></li>
    <li><span class="track-no">7</span><span class="track-name">Relax dummy</span><span class="track-time">4:15</span></li>
    <li><span class="track-no">8</span><span class="track-name">Dummy Relax</span><span class="track-time">6:10</span></li>
    <li><span class="track-no">9</span><span class="track-name">Piano Relax</span><span class="track-time">3:45</span></li>
    <li><span class="track-no">10</span><span class="track-name">Relax dummy copy</span><span class="track-time">7:15</span></li>
    <li><span class="track-no">11</span><span class="track-name">Relax dummy</span><span class="track-time">7:15</span></li>
    <li><span class="track-no">12</span><span class="track-name">Dummy Relax</span><span class="track-time">5:30</span></li>
  </ol>
</section>

<section class="panel inside-cover" aria-label="Inside cover">
  <div class="cloud-band" role="img" aria-label="Soft white clouds drifting across the top"></div>
  <div class="credit-block">
    <h2 class="album-title"><strong>Declarations:</strong><br>Sunrise Chants</h2>
    <p class="credit-line" style="margin-top:6px">All songs written by Beren Holvathy</p>
    <p class="credit-line">Copyright Berentones 2016</p>
  </div>
  <ol class="track-list">
    <li><span class="track-no">1</span><span class="track-name">Piano Relax</span><span class="track-time">5:30</span></li>
    <li><span class="track-no">2</span><span class="track-name">Relax dummy copy</span><span class="track-time">4:15</span></li>
    <li><span class="track-no">3</span><span class="track-name">Relax dummy</span><span class="track-time">6:10</span></li>
    <li><span class="track-no">4</span><span class="track-name">Dummy Relax</span><span class="track-time">3:45</span></li>
    <li><span class="track-no">5</span><span class="track-name">Piano Relax</span><span class="track-time">7:15</span></li>
    <li><span class="track-no">6</span><span class="track-name">Relax dummy copy</span><span class="track-time">5:30</span></li>
    <li><span class="track-no">7</span><span class="track-name">Relax dummy</span><span class="track-time">4:15</span></li>
    <li><span class="track-no">8</span><span class="track-name">Dummy Relax</span><span class="track-time">6:10</span></li>
    <li><span class="track-no">9</span><span class="track-name">Piano Relax</span><span class="track-time">3:45</span></li>
    <li><span class="track-no">10</span><span class="track-name">Relax dummy copy</span><span class="track-time">7:15</span></li>
    <li><span class="track-no">11</span><span class="track-name">Relax dummy</span><span class="track-time">7:15</span></li>
    <li><span class="track-no">12</span><span class="track-name">Dummy Relax</span><span class="track-time">5:30</span></li>
  </ol>
</section>

<section class="panel disc-tray" aria-label="Under the disc">
  <div class="cloud-band" role="img" aria-label="Soft white clouds drifting across the top"></div>
  <div class="tray-ring"></div>
</section>

<section class="disc" aria-label="Disc label">
  <svg width="400" height="400" viewBox="0 0 400 400" style="position:absolute;left:0;top:0">
    <defs>
      <radialGradient id="discFace" cx="50%" cy="45%" r="55%">
        <stop offset="0%" stop-color="#ffffff"/>
        <stop offset="85%" stop-color="#fafafa"/>
        <stop offset="100%" stop-color="#e6e6e6"/>
      </radialGradient>
      <path id="discEdge" d="M 200 200 m -172 0 a 172 172 0 0 0 344 0"/>
    </defs>
    <circle cx="200" cy="200" r="199" fill="url(#discFace)" stroke="#cfcfcf" stroke-width="1.5"/>
    <circle cx="200" cy="200" r="63" fill="none" stroke="#555" stroke-width="1"/>
    <circle cx="200" cy="200" r="57" fill="none" stroke="#999" stroke-width="0.8"/>
    <circle cx="200" cy="200" r="50" fill="#f1f1f1" stroke="#cfcfcf" stroke-width="1"/>
    <text class="disc-edge-text" dy="10">
      <textPath href="#discEdge" startOffset="50%" text-anchor="middle">All songs written by <tspan class="strong">Beren Holvathy</tspan>  -  Copyright <tspan class="strong">Berentones</tspan> 2016  -  <tspan class="strong">www.berentones.net</tspan></textPath>
    </text>
  </svg>
  <div class="bird-art" role="img" aria-label="Golden origami bird with small white clouds on its wing"></div>
  <div class="bird-shadow"></div>
  <h2 class="album-title"><strong>Declarations:</strong> Sunrise Chants</h2>
  <div class="artist-name"><span class="artist-mark"></span>Beren Holvathy</div>
</section>

</body>
</html>
```